NEW YORK Plumbing/utility company 10 year anniversary business card

Looking For simple back and front business card would like to include a few things in description
We offer 24/7 emergency service
residential
commercial
industrial
municipal
services offered
Plumbing
hydro excavation
hydro jetting
Well pumps
Sewer pumps
water mains
sewer mains

```html
<!DOCTYPE html>
<html lang="en">
<head>
<meta charset="utf-8">
<title>Ridgeline Water &amp; Sewer – Business Card</title>
<link rel="stylesheet" href="https://fonts.googleapis.com/css2?family=Montserrat:wght@500;600;700;800&display=swap">
<style>
  :root {
    --backdrop: #3b3b3b;
    --card: #1b1b1c;
    --blue: #2e9fe0;
    --blue-deep: #1f73b8;
    --white: #f2f2f2;
    --emboss: #2c2c2e;
  }
  * { box-sizing: border-box; margin: 0; padding: 0; }
  html, body {
    width: 1200px; height: 801px; overflow: hidden;
    background: var(--backdrop);
    font-family: "Montserrat", sans-serif;
  }
  .stage {
    width: 1200px; height: 801px;
    display: flex; align-items: center; justify-content: center; gap: 50px;
  }
  .card {
    width: 525px; height: 300px;
    background: var(--card);
    border-bottom: 3px solid var(--blue);
    border-left: 2px solid var(--blue);
    position: relative;
    color: var(--white);
  }
  /* Front */
  .front { padding: 48px 46px; display: flex; flex-direction: column; justify-content: space-between; }
  .brand { display: flex; align-items: center; gap: 14px; }
  .brand-dot { width: 26px; height: 26px; border-radius: 50%; background: var(--blue-deep); flex: none; }
  .brand-name {
    font-weight: 800; font-size: 30px; letter-spacing: 2px; line-height: 1.1;
    color: var(--blue-deep); text-transform: uppercase;
  }
  .tagline { font-weight: 800; font-size: 19px; color: var(--blue); letter-spacing: .3px; }
  .sectors { font-weight: 500; font-size: 14px; margin-top: 6px; letter-spacing: .3px; }
  .rule { height: 1px; background: var(--blue); margin: 12px 0; }
  .contact { display: flex; gap: 34px; font-size: 14px; font-weight: 500; }
  .contact span { display: flex; align-items: center; gap: 8px; }
  .contact svg { width: 14px; height: 14px; fill: var(--blue); }
  /* Back */
  .back { display: flex; align-items: center; padding: 0 34px 0 40px; }
  .back-brand { flex: 1; display: flex; align-items: center; gap: 12px; }
  .back-brand .brand-dot { background: var(--emboss); }
  .back-brand .brand-name { color: var(--emboss); font-size: 26px; }
  .divider { width: 1px; height: 190px; background: var(--blue); margin: 0 26px; }
  .services h2 { font-weight: 700; font-size: 17px; color: var(--blue); margin-bottom: 8px; }
  .services ul { list-style: none; }
  .services li { display: flex; align-items: center; gap: 9px; font-size: 14.5px; font-weight: 500; line-height: 1.6; }
  .services svg { width: 9px; height: 12px; fill: var(--blue); flex: none; }
</style>
</head>
<body>
<main class="stage">
  <section class="card front">
    <div class="brand">
      <span class="brand-dot"></span>
      <h1 class="brand-name">Ridgeline<br>Water &amp; Sewer</h1>
    </div>
    <div class="details">
      <p class="tagline">WE OFFER 24/7 EMERGENCY SERVICE</p>
      <p class="sectors">Residential • Commercial • Industrial • Municipal</p>
      <div class="rule"></div>
      <div class="contact">
        <span><svg viewBox="0 0 24 24"><path d="M6.6 10.8a15.1 15.1 0 0 0 6.6 6.6l2.2-2.2a1 1 0 0 1 1-.25 11.4 11.4 0 0 0 3.6.57 1 1 0 0 1 1 1V20a1 1 0 0 1-1 1A17 17 0 0 1 3 4a1 1 0 0 1 1-1h3.5a1 1 0 0 1 1 1c0 1.25.2 2.45.57 3.57a1 1 0 0 1-.25 1z"/></svg>555-014-7720</span>
        <span><svg viewBox="0 0 24 24"><path d="M2 5h20v14H2zm2 2v.5l8 5 8-5V7l-8 5z"/></svg>info@ridgelinews.com</span>
      </div>
    </div>
  </section>

  <section class="card back">
    <div class="back-brand">
      <span class="brand-dot"></span>
      <p class="brand-name">Ridgeline<br>Water &amp; Sewer</p>
    </div>
    <div class="divider"></div>
    <div class="services">
      <h2>Services Offered</h2>
      <ul>
        <li><svg viewBox="0 0 10 14"><path d="M5 0C5 0 0 6 0 9a5 5 0 0 0 10 0C10 6 5 0 5 0z"/></svg>Plumbing</li>
        <li><svg viewBox="0 0 10 14"><path d="M5 0C5 0 0 6 0 9a5 5 0 0 0 10 0C10 6 5 0 5 0z"/></svg>Hydro Excavation</li>
        <li><svg viewBox="0 0 10 14"><path d="M5 0C5 0 0 6 0 9a5 5 0 0 0 10 0C10 6 5 0 5 0z"/></svg>Hydro Jetting</li>
        <li><svg viewBox="0 0 10 14"><path d="M5 0C5 0 0 6 0 9a5 5 0 0 0 10 0C10 6 5 0 5 0z"/></svg>Well Pumps</li>
        <li><svg viewBox="0 0 10 14"><path d="M5 0C5 0 0 6 0 9a5 5 0 0 0 10 0C10 6 5 0 5 0z"/></svg>Sewer Pumps</li>
        <li><svg viewBox="0 0 10 14"><path d="M5 0C5 0 0 6 0 9a5 5 0 0 0 10 0C10 6 5 0 5 0z"/></svg>Water Mains</li>
        <li><svg viewBox="0 0 10 14"><path d="M5 0C5 0 0 6 0 9a5 5 0 0 0 10 0C10 6 5 0 5 0z"/></svg>Sewer Mains</li>
      </ul>
    </div>
  </section>
</main>
</body>
</html>
```